Visitenkarten-Design für italienisches Küchenschiff
Zielgruppe
Restaurantschiff Morvella
Aufgabenstellung
Wir sind ein italienische Küche Schiff auf der Binnenalster in Hamburg und wollen den schönen Blick und gerne auch die italienischen Farben widerspiegeln...ich brauche das einmal neutral für den normalen Gast....und würde das denn..wenn es denn gut wird...auch gerne individell mit m e i n e r Tel Nr und auch für meine führenden Mitarbeiter personalisieren...aber...zuerst natürlich das neutrale...dazu schicke ich die alte Karte mit dem auch alten Logo was nicht unbedingt verwendet werden muss...

```html
<!DOCTYPE html>
<html lang="de">
<head>
<meta charset="utf-8">
<title>Morvella – Visitenkarten</title>
<link href="https://fonts.googleapis.com/css2?family=Advent+Pro:wght@300;400&family=Dosis:wght@400&display=swap" rel="stylesheet">
<style>
  :root {
    --page: #4a4a4a;
    --card-warm: #45403f;
    --card-dark: #363636;
    --card-light: #ffffff;
    --text: #8c8076;
    --brand-dark: #1e1e1e;
    --brand-light: #111111;
    --rule: #7a6d62;
    --green: #009a5a;
    --white: #f4f4f4;
    --grey: #cfcfcf;
    --red: #a8343a;
  }
  * { margin: 0; padding: 0; box-sizing: border-box; }
  html, body { width: 1200px; height: 1200px; overflow: hidden; }
  body { background: var(--page); position: relative; font-family: "Advent Pro", "Arial Narrow", sans-serif; font-weight: 300; color: var(--text); }

  .card { position: absolute; width: 510px; height: 329px; box-shadow: 4px 5px 8px rgba(0,0,0,.45); overflow: hidden; }
  .card--warm { background: linear-gradient(135deg, #47423f, #423e3d); }
  .card--dark { background: var(--card-dark); }
  .card--light { background: var(--card-light); }
  .front { left: 61px; }
  .back { left: 628px; }
  .row-1 { top: 36px; } .row-2 { top: 411px; } .row-3 { top: 794px; }

  /* front */
  .flag-side { position: absolute; left: 0; top: 0; width: 14px; height: 100%; display: flex; flex-direction: column; }
  .flag-side span, .flag-bar span { flex: 1; }
  .flag-green { background: var(--green); }
  .flag-white { background: var(--white); }
  .card--light .flag-white { background: var(--grey); }
  .flag-red { background: var(--red); }

  .person { position: absolute; left: 50px; width: 140px; top: 142px; text-align: center; font-family: "Dosis", sans-serif; font-size: 24px; letter-spacing: 2px; line-height: 27px; color: var(--text); }
  .divider { position: absolute; left: 225px; top: 62px; width: 1px; height: 239px; background: var(--rule); }
  .brand { position: absolute; left: 262px; top: 84px; display: flex; align-items: center; gap: 10px; }
  .brand-name { font-family: "Dosis", sans-serif; font-size: 36px; line-height: 1; letter-spacing: 1px; color: var(--brand-dark); }
  .brand-dot { width: 14px; height: 14px; border-radius: 50%; background: var(--brand-dark); }
  .card--light .brand-name { color: var(--brand-light); }
  .card--light .brand-dot { background: var(--brand-light); }
  .brand-sub { position: absolute; left: 262px; top: 122px; font-family: "Dosis", sans-serif; font-size: 17px; letter-spacing: 1px; color: var(--brand-dark); }
  .card--light .brand-sub { color: var(--brand-light); }
  .contact { position: absolute; left: 262px; top: 155px; font-size: 16px; line-height: 19.5px; }
  .contact .label { font-size: 18px; margin-top: 3px; }

  /* back */
  .photo { position: absolute; left: 22px; width: 211px; }
  .photo--deck { top: 20px; height: 128px; background: linear-gradient(180deg, #8a6a4a 0%, #b68552 10%, #4f7f9a 22%, #7ca6c4 45%, #3d6a8e 58%, #9c2e33 72%, #e8e6e2 85%, #c9c6c0 100%); }
  .photo--night { top: 163px; height: 125px; background: linear-gradient(180deg, #6b5767 0%, #8a7385 25%, #4a4352 55%, #c8a872 66%, #2e2f3a 78%, #3a3c4a 100%); }
  .info { position: absolute; left: 257px; }
  .info h2 { font-weight: 300; font-size: 21px; line-height: 24px; }
  .info p { font-size: 16.5px; line-height: 21px; }
  .info--hours { top: 44px; width: 220px; }
  .hours-row { display: flex; justify-content: space-between; margin-top: 3px; }
  .kitchen { text-align: right; margin-top: 4px; }
  .info--booking { top: 178px; width: 245px; }
  .info--booking h2 { margin-bottom: 3px; }
  .info-rule { position: absolute; left: 302px; top: 151px; width: 122px; height: 1px; background: var(--rule); }
  .flag-bar { position: absolute; left: 0; right: 0; top: 300px; height: 9px; display: flex; }
</style>
</head>
<body>

<!-- Row 1 -->
<section class="card card--warm front row-1">
  <div class="flag-side"><span class="flag-green"></span><span class="flag-white"></span><span class="flag-red"></span></div>
  <div class="person">Pers. Name<br>Jobtitel</div>
  <div class="divider"></div>
  <div class="brand"><span class="brand-name">MORVELLA</span><span class="brand-dot"></span></div>
  <div class="brand-sub">Schiffsrestaurant Morvella</div>
  <div class="contact">
    Uferkai (Wasserseite)<br>20095 Hamburg
    <div class="label">Kontakt</div>
    Tel: +49 040 / 55 81 46<br>Fax:&nbsp;&nbsp; +49 040 / 55 81 4<br>www.seeschiff-morvella.de<br>E-Mail: info(at)seeschiff-morvella.de
  </div>
</section>
<section class="card card--warm back row-1">
  <div class="photo photo--deck" role="img" aria-label="Foto: Blick aus dem Schiffssalon auf die Binnenalster, gedeckter Tisch"></div>
  <div class="photo photo--night" role="img" aria-label="Foto: Alsterufer bei Nacht mit Lichtern im Wasser"></div>
  <div class="info info--hours"><h2>Öffnungszeiten</h2><p class="hours-row"><span>Montag - Sonntag</span><span>12:00 - 23:00</span></p><p class="kitchen">Küche bis 22:00</p></div>
  <div class="info-rule"></div>
  <div class="info info--booking"><h2>Reservierungen</h2><p>Wollen Sie einen Tisch reservieren? Wir freuen uns auf Ihren Anruf oder eine: reservierung(at)seeschiff-morvella.de</p></div>
  <div class="flag-bar"><span class="flag-green"></span><span class="flag-white"></span><span class="flag-red"></span></div>
</section>

<!-- Row 2 -->
<section class="card card--dark front row-2">
  <div class="flag-side"><span class="flag-green"></span><span class="flag-white"></span><span class="flag-red"></span></div>
  <div class="person">Pers. Name<br>Jobtitel</div>
  <div class="divider"></div>
  <div class="brand"><span class="brand-name" style="color:#0e0e0e">MORVELLA</span><span class="brand-dot" style="background:#0e0e0e"></span></div>
  <div class="brand-sub" style="color:#0e0e0e">Schiffsrestaurant Morvella</div>
  <div class="contact">
    Uferkai (Wasserseite)<br>20095 Hamburg
    <div class="label">Kontakt</div>
    Tel: +49 040 / 55 81 46<br>Fax:&nbsp;&nbsp; +49 040 / 55 81 4<br>www.seeschiff-morvella.de<br>E-Mail: info(at)seeschiff-morvella.de
  </div>
</section>
<section class="card card--dark back row-2">
  <div class="photo photo--deck" role="img" aria-label="Foto: Blick aus dem Schiffssalon auf die Binnenalster, gedeckter Tisch"></div>
  <div class="photo photo--night" role="img" aria-label="Foto: Alsterufer bei Nacht mit Lichtern im Wasser"></div>
  <div class="info info--hours"><h2>Öffnungszeiten</h2><p class="hours-row"><span>Montag - Sonntag</span><span>12:00 - 23:00</span></p><p class="kitchen">Küche bis 22:00</p></div>
  <div class="info-rule"></div>
  <div class="info info--booking"><h2>Reservierungen</h2><p>Wollen Sie einen Tisch reservieren? Wir freuen uns auf Ihren Anruf oder eine: reservierung(at)seeschiff-morvella.de</p></div>
  <div class="flag-bar"><span class="flag-green"></span><span class="flag-white"></span><span class="flag-red"></span></div>
</section>

<!-- Row 3 -->
<section class="card card--light front row-3">
  <div class="flag-side"><span class="flag-green"></span><span class="flag-white"></span><span class="flag-red"></span></div>
  <div class="person">Pers. Name<br>Jobtitel</div>
  <div class="divider"></div>
  <div class="brand"><span class="brand-name">MORVELLA</span><span class="brand-dot"></span></div>
  <div class="brand-sub">Schiffsrestaurant Morvella</div>
  <div class="contact">
    Uferkai (Wasserseite)<br>20095 Hamburg
    <div class="label">Kontakt</div>
    Tel: +49 040 / 55 81 46<br>Fax:&nbsp;&nbsp; +49 040 / 55 81 4<br>www.seeschiff-morvella.de<br>E-Mail: info(at)seeschiff-morvella.de
  </div>
</section>
<section class="card card--light back row-3">
  <div class="photo photo--deck" role="img" aria-label="Foto: Blick aus dem Schiffssalon auf die Binnenalster, gedeckter Tisch"></div>
  <div class="photo photo--night" role="img" aria-label="Foto: Alsterufer bei Nacht mit Lichtern im Wasser"></div>
  <div class="info info--hours"><h2>Öffnungszeiten</h2><p class="hours-row"><span>Montag - Sonntag</span><span>12:00 - 23:00</span></p><p class="kitchen">Küche bis 22:00</p></div>
  <div class="info info--booking"><h2>Reservierungen</h2><p>Wollen Sie einen Tisch reservieren? Wir freuen uns auf Ihren Anruf oder eine: reservierung(at)seeschiff-morvella.de</p></div>
  <div class="flag-bar"><span class="flag-green"></span><span class="flag-white"></span><span class="flag-red"></span></div>
</section>

</body>
</html>
```